BRIGHT COLORFUL + 55 FAMILY HISTORY BROCHURE 11 x 17 bifold

11 x 17 Bifold Flyer I have given you the Layout I just need you to make it Pretty

YOU DO NOT NEED TO FOLLOW MY LAYOUT, You can but dont have too

Target Market(s)

55 year old consumers, who could choose our service of Hereditary Cancer Screening

Industry/Entity Type

Health And Wellness

Requirements
Must have
• Must be appealing to Grand Parents, must make them want to test , show lots of pictures of grand children, YOU DO NOT NEED TO FOLLOW MY LAYOUT , You can but dont have too
Nice to have
• use our colors of our logo , YOU DO NOT NEED TO FOLLOW MY LAYOUT , You can but dont have too
Should not have
• YOU DO NOT NEED TO FOLLOW MY LAYOUT, You can but dont have too

```html
<!DOCTYPE html>
<html lang="en">
<head>
<meta charset="utf-8">
<title>Hereditary Cancer Screening – Bifold Brochure</title>
<link href="https://fonts.googleapis.com/css2?family=Bebas+Neue&family=Oswald:wght@300&family=Montserrat:wght@400;600;700;800&display=swap" rel="stylesheet">
<style>
  :root {
    --navy: #0d1b4a;
    --green: #7ccf2a;
    --green-dark: #5fb31b;
    --red: #e0201f;
    --ink: #1c2333;
    --paper: #ffffff;
    --backdrop: #c9cacd;
  }
  * { margin: 0; padding: 0; box-sizing: border-box; }
  html, body { width: 1200px; height: 1200px; overflow: hidden; }
  body {
    background: var(--backdrop);
    font-family: "Montserrat", Arial, sans-serif;
    color: var(--ink);
    position: relative;
  }
  .spread-frame {
    position: absolute;
    left: 50px; top: 211px;
    width: 1100px; height: 778px;
    box-shadow: 0 14px 30px rgba(0,0,0,.25);
  }
  .spread {
    position: absolute; left: 0; top: 0;
    width: 806px; height: 570px;
    transform: scale(1.3648);
    transform-origin: 0 0;
    background: var(--paper);
    overflow: hidden;
  }
  .spread-art { position: absolute; inset: 0; width: 806px; height: 570px; }
  .panel-text { position: absolute; }

  /* left panel */
  .intro { left: 20px; top: 305px; width: 370px; }
  .intro-question { font-size: 12px; color: var(--navy); font-weight: 400; }
  .intro-question b { font-weight: 800; }
  .intro-swab { font-size: 11.5px; color: var(--green-dark); margin-top: 4px; }
  .intro-swab b { font-weight: 700; }
  .intro-lead { font-size: 8.6px; color: var(--navy); font-weight: 600; margin-top: 13px; line-height: 1.5; }
  .intro-belief { font-size: 11px; color: var(--green-dark); font-weight: 600; margin-top: 9px; line-height: 1.35; }
  .intro-body { font-size: 7.8px; color: var(--navy); margin-top: 7px; line-height: 1.7; }

  .brand { display: flex; align-items: center; gap: 4px; }
  .brand-mark { border-radius: 50%; background: var(--navy); flex: none; }
  .brand-name {
    color: var(--navy); font-weight: 600; text-transform: uppercase;
    line-height: 1; border-left: 1px solid var(--navy);
  }
  .brand--small { position: absolute; left: 158px; top: 494px; }
  .brand--small .brand-mark { width: 22px; height: 22px; }
  .brand--small .brand-name { font-size: 8.5px; padding-left: 4px; }

  .web { position: absolute; top: 549px; font-size: 7.5px; color: #fff; text-align: center; width: 403px; }
  .web--left { left: 0; }
  .web--right { left: 403px; }

  /* right panel */
  .cover { left: 414px; top: 16px; width: 386px; text-align: center; }
  .cover-title {
    font-family: "Bebas Neue", Impact, sans-serif;
    font-size: 55px; color: var(--navy); line-height: .95; letter-spacing: 0;
  }
  .cover-screening {
    font-family: "Oswald", Arial, sans-serif; font-weight: 300;
    font-size: 48px; color: var(--green); letter-spacing: 16px;
    line-height: 1; margin-top: 2px; margin-right: -16px;
  }
  .cover-quote { font-size: 12px; color: var(--navy); margin-top: 9px; letter-spacing: .3px; }
  .cover-ask { font-size: 16.5px; font-weight: 600; color: var(--green-dark); margin-top: 5px; }
  .cover-ask .loved { color: var(--red); }
  .cover-ask .ones { color: var(--navy); }
  .cover-ask-sub { font-size: 7.5px; color: var(--navy); margin-top: 3px; }
  .cover-gift { font-size: 8.5px; color: var(--navy); margin-top: 12px; }
  .cover-knowing { font-size: 11.5px; color: var(--green-dark); margin-top: 2px; }
  .cover-power { font-size: 12.5px; font-weight: 700; color: var(--navy); margin-top: 2px; }
  .brand--cover { position: absolute; left: 544px; top: 267px; }
  .brand--cover .brand-mark { width: 38px; height: 38px; }
  .brand--cover .brand-name { font-size: 12.5px; padding-left: 5px; line-height: 1.05; }
</style>
</head>
<body>
<div class="spread-frame">
  <div class="spread">
    <svg class="spread-art" viewBox="0 0 806 570" xmlns="http://www.w3.org/2000/svg">
      <defs>
        <linearGradient id="heroTone" x1="0" y1="0" x2="1" y2="0.6">
          <stop offset="0" stop-color="#f1e6dc"/>
          <stop offset=".45" stop-color="#ecd6c4"/>
          <stop offset=".8" stop-color="#e6e8ee"/>
          <stop offset="1" stop-color="#aebcd6"/>
        </linearGradient>
        <linearGradient id="heroFade" x1="0" y1="0" x2="0" y2="1">
          <stop offset=".5" stop-color="#fff" stop-opacity="0"/>
          <stop offset=".95" stop-color="#fff" stop-opacity="1"/>
        </linearGradient>
        <linearGradient id="handsTone" x1="0" y1="0" x2="1" y2="1">
          <stop offset="0" stop-color="#8aa866"/>
          <stop offset=".4" stop-color="#d8b49c"/>
          <stop offset=".75" stop-color="#e3c0a7"/>
          <stop offset="1" stop-color="#6f8fc4"/>
        </linearGradient>
        <linearGradient id="familyA" x1="0" y1="0" x2="1" y2="1">
          <stop offset="0" stop-color="#cfd8b2"/><stop offset=".5" stop-color="#eccbd7"/><stop offset="1" stop-color="#e3c0a8"/>
        </linearGradient>
        <linearGradient id="familyB" x1="0" y1="0" x2="1" y2="1">
          <stop offset="0" stop-color="#b59a85"/><stop offset=".5" stop-color="#e8cbb6"/><stop offset="1" stop-color="#f3ebe2"/>
        </linearGradient>
        <linearGradient id="familyC" x1="0" y1="0" x2="1" y2="1">
          <stop offset="0" stop-color="#f2e0ae"/><stop offset=".5" stop-color="#ecd0bc"/><stop offset="1" stop-color="#94acd4"/>
        </linearGradient>
      </defs>

      <g role="img" aria-label="Photo of a smiling grandmother hugging her young granddaughter">
        <path d="M0,0 H292 C293,110 305,190 335,240 C320,265 300,285 290,300 H0 Z" fill="url(#heroTone)"/>
        <path d="M0,0 H292 C293,110 305,190 335,240 C320,265 300,285 290,300 H0 Z" fill="url(#heroFade)"/>
      </g>

      <rect class="band band--left" x="0" y="535" width="403" height="35" fill="var(--green)"/>

      <g role="img" aria-label="Photo of an older hand gently holding a child's hand">
        <path d="M403,382 C520,345 650,370 806,455 L806,570 L403,570 Z" fill="url(#handsTone)"/>
      </g>

      <path class="swoosh swoosh--navy" d="M292,0 C293,140 320,215 380,270 C430,315 500,360 560,400" fill="none" stroke="var(--navy)" stroke-width="9"/>
      <path class="swoosh swoosh--green" d="M321,0 C318,130 340,205 395,250" fill="none" stroke="var(--green)" stroke-width="5"/>
      <path class="swoosh swoosh--green" d="M403,382 C520,345 650,370 806,455" fill="none" stroke="var(--green)" stroke-width="5"/>

      <g class="photo-circle">
        <circle cx="422" cy="302" r="74" fill="var(--green)"/>
        <circle cx="422" cy="302" r="70" fill="#fff"/>
        <circle cx="422" cy="302" r="66" fill="url(#familyA)" role="img" aria-label="Photo of grandparents reading with their grandchildren"/>
      </g>
      <g class="photo-circle">
        <circle cx="572" cy="410" r="64" fill="var(--navy)"/>
        <circle cx="572" cy="410" r="59" fill="#fff"/>
        <circle cx="572" cy="410" r="55" fill="url(#familyB)" role="img" aria-label="Photo of a grandfather and grandmother smiling with a grandchild"/>
      </g>
      <g class="photo-circle">
        <circle cx="725" cy="449" r="54" fill="var(--green)"/>
        <circle cx="725" cy="449" r="50" fill="#fff"/>
        <circle cx="725" cy="449" r="46" fill="url(#familyC)" role="img" aria-label="Photo of a grandfather hugging his grandson"/>
      </g>
    </svg>

    <section class="panel-text intro">
      <p class="intro-question"><b>DOES CANCER</b> Run in Your Family?</p>
      <p class="intro-swab"><b>A Simple Swab</b> Could SAVE a Family Members LIFE</p>
      <p class="intro-lead">Your decision won't just affect you. It will also impact Your Family,<br>since your test results may Forecast Their Cancer Risks, too.</p>
      <p class="intro-belief">WE BELIEVE IT IS IMPORTANT TO UNDERSTAND WHAT<br>CAN AND CANNOT BE LEARNED WITH GENETIC TESTING.</p>
      <p class="intro-body">Genetic mutations can increase risks for certain cancers, but this does not mean<br>cancer will definitely develop. You should be prepared to receive positive or<br>negative results. Most people receive Negative Results  meaning no mutations<br>associated with an increased risk for the Hereditary cancers.</p>
    </section>

    <div class="brand brand--small">
      <span class="brand-mark"></span>
      <span class="brand-name">Kinward<br>Health<br>Group</span>
    </div>

    <p class="web web--left">www.kinwardscreening.com</p>

    <section class="panel-text cover">
      <h1 class="cover-title">Hereditary Cancer</h1>
      <p class="cover-screening">SCREENING</p>
      <p class="cover-quote">"THE TEST YOU TAKE FOR THEM"</p>
      <p class="cover-ask">WILL YOU GIVE YOUR <span class="loved">LOVED</span> <span class="ones">ONES</span></p>
      <p class="cover-ask-sub">The information to Beat Cancer in their lives?</p>
      <p class="cover-gift">GIVE THEM THE GIFT OF KNOWLEDGE</p>
      <p class="cover-knowing">KNOWING IS BETTER THAN</p>
      <p class="cover-power">KNOWLEDGE IS POWER</p>
    </section>

    <div class="brand brand--cover">
      <span class="brand-mark"></span>
      <span class="brand-name">Kinward<br>Health<br>Group</span>
    </div>

    <p class="web web--right">www.kinwardscreening.com</p>
  </div>
</div>
</body>
</html>
```